Maple Home Health Care of San Diego needs a brochure to advertise its services.

We need a brochure for a new company called Maple Home Health Care of San Diego, Inc. We provide skilled home health care services such as skilled nursing, physical, occupational, and speech therapy, medical social work, and home health aide services. Our patient population is mostly 65 years and older. We market our services in the community, including hospitals, skilled nursing and assisted living facilities, doctor's offices etc. We would like to see designs that are easy to read, go with our logo color, which is green, and includes pictures of multicultural elderly individuals receiving medical or rehab care in or surrounding the home. Please include the information contained in the files attached, which has our services, about home health care, and our mission and vision.
Maple Home Health Care of San Diego, Inc.
4827 Harbor Crest Lane, Suite 5B
Encinitas, CA 92031
760-418-LEAF (office)
76- 529-LEAF (fax)
760-284-5370 (cell)

Target Market(s)

See above

Industry/Entity Type

Home Health Care

Font styles to use
Sans Serif

Colors
9bcb3c
add136

Requirements
Must have
• Must be tri-fold and geared toward an elderly and medical field population. Please view some other home health agency brochures out there for examples.

```html
<!DOCTYPE html>
<html lang="en">
<head>
<meta charset="UTF-8">
<title>Home Health Services Brochure – Inside Spread</title>
<link href="https://fonts.googleapis.com/css2?family=Roboto:wght@400;500;700&display=swap" rel="stylesheet">
<style>
  :root {
    --page-bg: #f4f5f2;
    --green-deep: #2f7d1f;
    --green-mid: #469f27;
    --green-bright: #6cbb2f;
    --green-light: #9bcb3c;
    --green-pale: #add136;
    --text-light: #ffffff;
    --photo-warm: #d9d3cc;
    --photo-cool: #b9c2c8;
  }
  * { box-sizing: border-box; margin: 0; padding: 0; }
  html, body {
    width: 1200px; height: 1000px; overflow: hidden;
    background: var(--page-bg);
    font-family: "Roboto", Arial, sans-serif;
    color: var(--text-light);
  }
  .brochure {
    position: absolute; left: 50px; top: 75px;
    width: 1100px; height: 850px;
    display: grid; grid-template-columns: repeat(3, 1fr);
    background: linear-gradient(115deg, var(--green-deep) 0%, var(--green-mid) 40%, var(--green-bright) 75%, var(--green-light) 100%);
    box-shadow: 0 18px 40px rgba(0,0,0,0.18);
    overflow: hidden;
  }
  .panel { position: relative; padding: 34px 30px; border-right: 1px solid rgba(255,255,255,0.12); }
  .panel:last-child { border-right: none; }

  .panel-vision { padding: 0; display: flex; flex-direction: column; }
  .vision-block {
    position: relative; height: 470px; padding: 30px 30px;
    background: linear-gradient(160deg, #3a8e24 0%, var(--green-deep) 100%);
  }
  .vision-block::after {
    content: ""; position: absolute; left: 60px; bottom: -18px;
    border-left: 18px solid transparent; border-right: 18px solid transparent;
    border-top: 18px solid var(--green-deep);
  }
  .photo-care {
    flex: 1;
    background: linear-gradient(135deg, var(--photo-cool) 0%, var(--photo-warm) 55%, #e9e4de 100%);
  }

  .panel-title { font-size: 25px; font-weight: 700; margin-bottom: 12px; }
  .services-title { font-size: 24px; font-weight: 700; line-height: 1.2; margin-bottom: 22px; }
  .service { margin-bottom: 22px; }
  .service-name { font-size: 15px; font-weight: 700; margin-bottom: 4px; }
  .bullets { list-style: none; }
  .bullets li {
    position: relative; padding-left: 16px;
    font-size: 15px; line-height: 1.3; margin-bottom: 2px;
  }
  .bullets li::before {
    content: ""; position: absolute; left: 0; top: 7px;
    width: 7px; height: 7px; border-radius: 50%; background: var(--text-light);
  }
  .vision-list li { font-size: 16px; line-height: 1.32; margin-bottom: 4px; }

  .services-more-content { position: relative; z-index: 1; }
  .photo-dandelion {
    position: absolute; right: -40px; bottom: 40px;
    width: 360px; height: 360px; border-radius: 50%;
    background: radial-gradient(circle at 50% 50%, rgba(255,255,255,0.85) 0%, rgba(255,255,255,0.45) 30%, rgba(173,209,54,0.25) 55%, rgba(173,209,54,0) 72%);
  }
</style>
</head>
<body>
  <main class="brochure">
    <section class="panel panel-vision">
      <div class="vision-block">
        <h2 class="panel-title">Vision</h2>
        <ul class="bullets vision-list">
          <li>To be the provider of choice for quality home health care services, recognized for enduring dedication to provide innovative, professional, and compassionate care to the community we serve.</li>
          <li>To be one of the leading employers for healthcare professionals by providing our staff with an inviting work environment, competitive compensation and knowledgeable, trustworthy management and direction.</li>
          <li>To satisfy our patients’ needs and exceed their expectations by utilizing best practices and quality care standards.</li>
        </ul>
      </div>
      <div class="photo-care" role="img" aria-label="Photo of a smiling caregiver with an elderly man at home"></div>
    </section>

    <section class="panel panel-services">
      <h2 class="services-title">We provide the following services in the comfort of your home:</h2>
      <div class="service">
        <h3 class="service-name">Skilled Nursing</h3>
        <ul class="bullets">
          <li>Assess for changes in medical condition</li>
          <li>Education regarding disease management</li>
          <li>Teach how to manage and administer mediation</li>
          <li>Perform medical procedures such as catheter insertion, wound care, ostomy care, lab work and injections</li>
        </ul>
      </div>
      <div class="service">
        <h3 class="service-name">Physical Therapy</h3>
        <ul class="bullets">
          <li>Focus on exercises and activities to improve balance, strength, and endurance, to reduce the risk of falls</li>
          <li>Improve ability to ambulate and/or transfer</li>
          <li>Evaluate the need for and train in the use of devices such as walker, cane, wheelchair</li>
          <li>Instruct in home exercise program</li>
        </ul>
      </div>
      <div class="service">
        <h3 class="service-name">Occupational Therapy</h3>
        <ul class="bullets">
          <li>Focus on the ability to perform activities of daily living such as bathing, dressing, and household tasks</li>
          <li>Evaluate the need for and train in the use of adaptive equipment to aid in performing activities of daily living</li>
          <li>Teach energy conservation techniques</li>
          <li>Instruct in home exercise program</li>
        </ul>
      </div>
    </section>

    <section class="panel panel-services-more">
      <div class="photo-dandelion" role="img" aria-label="Photo of a dandelion seed head with seeds drifting away"></div>
      <div class="services-more-content">
        <div class="service">
          <h3 class="service-name">Speech Therapy</h3>
          <ul class="bullets">
            <li>Improve communication skills</li>
            <li>Focus on the ability to swallow safely</li>
            <li>Improve memory and cognition/thinking skills</li>
          </ul>
        </div>
        <div class="service">
          <h3 class="service-name">Medical Social Work</h3>
          <ul class="bullets">
            <li>Provide referrals to community resources</li>
            <li>Provide short-term counseling for patients and caregivers</li>
            <li>Assist with living arrangements, financial concerns, and long-term planning</li>
            <li>Focus on overall social and emotional health</li>
          </ul>
        </div>
        <div class="service">
          <h3 class="service-name">Home Health Aide</h3>
          <ul class="bullets">
            <li>Provided when you are receiving skilled nursing, physical, occupational, or speech therapy</li>
            <li>Help with personal care on a short-term basis, such as bathing, dressing, toileting, light meal prep</li>
          </ul>
        </div>
      </div>
    </section>
  </main>
</body>
</html>
```